Research, Writing and Editing business needs a Business Card Design

I need a business card design for a new company based in Melbourne called The Bellwood Advisory Group. We provide research, writing and editing services. The company logo is attached, but I am open to your creative designs for business cards with the logo. As you will note, there are two potential logos. Feel free to use either of the logos.

The overall look I am hoping for is sleek, sophisticated, feminine and elegant.

Thanks in advance for your efforts.

Target Market(s)

Business professionals, academics and students

Industry/Entity Type

Business

Font styles to use
Serif
Script

Colors

Designer to choose colors to be used in the design.

Requirements
Must have
• The Bellwood Advisory Group
Dr Tessa Brennig

M: 0458 293 647
E: tessa@thebellwoodadvisorygroup.com.au
W: thebellwoodadvisorygroup.com.au
Nice to have
• Research | Writing | Editing

```html
<!DOCTYPE html>
<html lang="en">
<head>
<meta charset="utf-8">
<title>The Bellwood Advisory Group — Business Card</title>
<link href="https://fonts.googleapis.com/css2?family=Cinzel:wght@400;600&family=Great+Vibes&display=swap" rel="stylesheet">
<style>
  :root {
    --backdrop: #1c1b1e;
    --card-black: #0f0e11;
    --card-edge: #2a282d;
    --violet: #8c66cc;
    --violet-light: #a88ae0;
    --ink-white: #e9e7ee;
    --ink-grey: #bdbac4;
    --disc-white: #f7f7f7;
    --logo-black: #151417;
  }
  * { margin: 0; padding: 0; box-sizing: border-box; }
  html, body {
    width: 1200px; height: 1134px; overflow: hidden;
    background: var(--backdrop);
  }
  .sheet {
    width: 1200px; height: 1134px;
    display: flex; flex-direction: column; align-items: center; justify-content: center;
    gap: 64px;
  }
  .card {
    position: relative;
    width: 770px; height: 440px;
    border-radius: 6px;
    overflow: hidden;
    box-shadow: 0 18px 40px rgba(0,0,0,.55);
  }
  /* Front */
  .card--front { background: var(--card-black); border: 1px solid var(--card-edge); }
  .brand {
    position: absolute; left: 56px; top: 50px;
    display: flex; align-items: center; gap: 14px;
  }
  .brand__mark {
    width: 26px; height: 26px; background: var(--ink-grey); border-radius: 3px;
  }
  .brand__name {
    font-family: "Cinzel", serif; font-weight: 400;
    font-size: 19px; letter-spacing: 2.5px; color: var(--ink-white);
  }
  .person { position: absolute; left: 56px; top: 150px; }
  .person__name {
    font-family: "Great Vibes", cursive; font-size: 50px; line-height: 1;
    color: var(--violet-light);
  }
  .person__title {
    margin: 8px 0 0 120px;
    font-family: "Cinzel", serif; font-size: 15px; letter-spacing: 3px;
    color: var(--ink-white);
  }
  .contact {
    position: absolute; left: 56px; top: 268px;
    list-style: none;
    font-family: "Cinzel", serif; font-size: 14px; letter-spacing: 1.2px;
    color: var(--ink-white);
  }
  .contact__row { display: flex; align-items: center; gap: 12px; height: 30px; }
  .contact__icon { width: 20px; height: 20px; flex: none; }
  .accent-lines {
    position: absolute; right: 140px; top: 0; height: 100%;
    display: flex; gap: 16px;
  }
  .accent-lines span {
    display: block; width: 6px; height: 100%;
    background: linear-gradient(180deg, var(--violet-light), var(--violet));
  }
  /* Back */
  .card--back {
    background: radial-gradient(circle at 50% 50%, #3a383d 0%, #17161a 70%);
    border: 1px solid var(--card-edge);
    display: flex; align-items: center; justify-content: center;
  }
  .disc {
    width: 340px; height: 340px; border-radius: 50%;
    background: var(--disc-white);
    display: flex; flex-direction: column; align-items: center; justify-content: center;
    gap: 14px;
    box-shadow: 0 0 30px rgba(255,255,255,.15);
  }
  .disc__mark { width: 22px; height: 22px; background: var(--logo-black); border-radius: 3px; }
  .disc__name {
    font-family: "Cinzel", serif; font-weight: 400;
    font-size: 19px; letter-spacing: 2px; line-height: 1.5;
    color: var(--logo-black); text-align: center;
  }
</style>
</head>
<body>
<main class="sheet">
  <section class="card card--front" aria-label="Business card front">
    <div class="brand">
      <span class="brand__mark"></span>
      <span class="brand__name">The Bellwood Advisory Group</span>
    </div>
    <div class="person">
      <p class="person__name">Dr Tessa Brennig</p>
      <p class="person__title">JOB TITLE</p>
    </div>
    <ul class="contact">
      <li class="contact__row">
        <svg class="contact__icon" viewBox="0 0 20 20" aria-hidden="true"><circle cx="10" cy="10" r="10" fill="#8c66cc"/><path d="M7 5h2l1 3-1.5 1a6 6 0 0 0 2.5 2.5L12 10l3 1v2c0 1-1 2-2 2A8 8 0 0 1 5 7c0-1 1-2 2-2z" fill="#0f0e11"/></svg>
        <span>0458 293 647</span>
      </li>
      <li class="contact__row">
        <svg class="contact__icon" viewBox="0 0 20 20" aria-hidden="true"><circle cx="10" cy="10" r="10" fill="#8c66cc"/><rect x="5" y="6.5" width="10" height="7" fill="none" stroke="#0f0e11" stroke-width="1.4"/><path d="M5 6.5l5 4 5-4" fill="none" stroke="#0f0e11" stroke-width="1.4"/></svg>
        <span>tessa@thebellwoodadvisorygroup.com.au</span>
      </li>
      <li class="contact__row">
        <svg class="contact__icon" viewBox="0 0 20 20" aria-hidden="true"><circle cx="10" cy="10" r="10" fill="#8c66cc"/><circle cx="10" cy="10" r="5" fill="none" stroke="#0f0e11" stroke-width="1.3"/><path d="M5 10h10M10 5c-2.5 3-2.5 7 0 10M10 5c2.5 3 2.5 7 0 10" fill="none" stroke="#0f0e11" stroke-width="1.1"/></svg>
        <span>thebellwoodadvisorygroup.com.au</span>
      </li>
    </ul>
    <div class="accent-lines" aria-hidden="true"><span></span><span></span></div>
  </section>

  <section class="card card--back" aria-label="Business card back">
    <div class="disc">
      <span class="disc__mark"></span>
      <span class="disc__name">The Bellwood<br>Advisory Group</span>
    </div>
  </section>
</main>
</body>
</html>
```